Manuka honey wholesales and export company needs a website

We are a Manuka honey Wholesale and export company based in New Zealand and needing a website to attract new clients.
We produce one of the worlds best honeys so we need a clean, modern look that lets everybody know that we can supply our product around the world.
We source only the finest Manuka honey from some of the most remote parts of New Zealand and send it around the world for everyone to enjoy.
We need a website that will allow people to inquire about export or bulk purchasing as well as a buying tab with pricing but one that we can add photos to as our product labels are not complete yet.
We also support and supply local farmers markets and a page dedicated to this would be good with details on when and where they are.

Here are links to other manuka honey websites to get an idea
http://www.hivelarkfields.co.nz/
http://www.pellora.co.nz/key-ingredients/manuka-honey/nz100008?gclid=Xq7PLmRtYvBNsKdWoEjZaHuFcGiTeLpOyNbRkVwQmXsDaJzUoKiHnCtFgPlEbYrAqMdSvZuWxTeNoGjHkLrPfIsBaCqZyDm

Target Market(s)

The general public, retail shops and exporters

Industry/Entity Type

Health And Wellness

Number of Pages Required

5+ page

Font styles to use
Serif

Requirements
Must have
• 1. A page and contact details for Export and wholesale inquiries
• Desmond Harlow
• Export manager
• +64 21 438 190
• dkharlow@pelmail.co.nz
• 2. Page for the farmers market we supply our product to.
• Details....
• Contact: Neil Forbes
• +64 21 067 4183
• tideflowernz@mailpost.com
• MARKET INFORMATION
• Quaywell Market
• The market operates year round and is located on Ferndell Square.*
• http://quaywell.org/sol-verde-market/
• Saturday 8am-1pm
• Sunday 9am-1pm
• Ashgrove Hamlet Market
• http://www.ashgrovegrowersmarket.co.nz/
• 64 Paddock Ln, Oakhurst, Auckland 2469, New Zealand
• Market is held each Sunday from 8:30am-1pm.
• 3. An information page on manuka honey....i will attach info but most of the info you can find on other manuka honey websites..
• Health benefits..
• There are two main components of Manuka honey which give it many health benefits:
• - Hydrogen peroxide, a naturally antibiotic found in Manuka honey.
• - Methylglyoxal (MG). A powerful antibiotic compound found in large quantities in Manuka honey.
• What is MGO?
• The MGO indicates the amount of Methylglyoxal in the honey. The higher the MGO rating the more antibacterial properties are in the honey.
• Proven health Benefits of Active Manuka are....
• Aiding in the treatment of:
• - -Common Cold and Flu
• - -sore throats
• - -cuts and abrasions
• - -Reduce hair loss and scalp problems
• - -treating fungal infections
• - -Burns
• - -ulsers
• - -strengthening the immune system
• 4. A product page with a range of our products with a link yo by direct from us
• The details for this page will need to be added later as we are still doing our range!
Nice to have
• Feel free to make up a mission statement or whatever inspires you to make this a great website.
Should not have
• Go crazy please! I trust you will come up with something amazing :)

```html
<!DOCTYPE html>
<html lang="en">
<head>
<meta charset="utf-8">
<title>Tideflower Honey NZ Limited</title>
<link rel="stylesheet" href="https://fonts.googleapis.com/css2?family=Roboto+Condensed:ital,wght@0,400;0,700;1,400;1,700&family=Roboto:wght@400;500&family=Cormorant+Garamond:ital,wght@1,500&display=swap">
<style>
:root{
  --honey:#f1d500;
  --honey-deep:#e3c300;
  --ink:#0d0d0d;
  --paper:#d2d0d1;
  --nav:#d6d4d5;
  --text:#2b2b2b;
  --muted:#4a4a4a;
  --white:#ffffff;
  --night:#1c1a18;
}
*{box-sizing:border-box;margin:0;padding:0}
html,body{width:1200px;height:2980px;overflow:hidden}
body{position:relative;background:var(--paper);font-family:"Roboto",Arial,sans-serif;color:var(--text)}
.cond{font-family:"Roboto Condensed","Arial Narrow",sans-serif}

/* header */
.site-header{position:absolute;top:0;left:0;width:1200px;height:70px;background:var(--nav)}
.brand{position:absolute;left:218px;top:0;width:174px;height:70px;background:var(--ink);display:flex;align-items:center;justify-content:center;gap:8px}
.brand-mark{width:12px;height:12px;background:var(--honey)}
.brand-name{font-family:"Roboto Condensed",sans-serif;font-weight:700;font-size:14px;color:var(--honey);white-space:nowrap}
.main-nav{position:absolute;left:432px;top:0;height:70px;display:flex;align-items:center;gap:32px}
.main-nav a{font-family:"Roboto Condensed",sans-serif;font-weight:700;font-size:11.5px;color:var(--ink);text-decoration:none;letter-spacing:.3px}

/* hero */
.hero{position:absolute;top:70px;left:0;width:1200px;height:648px;background:linear-gradient(180deg,#4a3826 0%,#6b4b22 40%,#8a5a1e 62%,#3a2a1c 100%)}
.hero-photo{position:absolute;inset:0;background:radial-gradient(ellipse 320px 220px at 640px 300px,rgba(230,150,30,.55),transparent 70%),radial-gradient(ellipse 160px 140px at 290px 180px,rgba(240,190,40,.5),transparent 70%),radial-gradient(ellipse 130px 120px at 960px 500px,rgba(240,180,20,.55),transparent 70%)}
.hero-copy{position:absolute;left:236px;top:240px;color:var(--white)}
.hero-welcome{font-family:"Cormorant Garamond",serif;font-style:italic;font-weight:500;font-size:46px;letter-spacing:4px;line-height:1}
.hero-title{font-family:"Roboto Condensed",sans-serif;font-weight:700;font-size:36px;color:var(--honey);letter-spacing:2px;margin-top:6px}
.hero-sub{font-family:"Roboto Condensed",sans-serif;font-weight:700;font-style:italic;font-size:21px;letter-spacing:1.2px;line-height:28px;margin-top:6px}
.btn{display:inline-flex;align-items:center;justify-content:center;border-radius:16px;font-family:"Roboto Condensed",sans-serif;font-weight:700;font-size:12px;letter-spacing:1px;text-decoration:none}
.btn-shop{position:absolute;left:234px;top:430px;width:144px;height:32px;background:var(--honey);color:var(--ink)}
.hero-dots{position:absolute;left:961px;top:340px;display:flex;flex-direction:column;gap:12px}
.hero-dots span{width:7px;height:7px;border-radius:50%;background:var(--honey)}

/* shared section */
.section{position:absolute;left:0;width:1200px;text-align:center}
.section-light{background:var(--paper)}
.section-dark{background:linear-gradient(180deg,#24211e,#141312)}
.h-main{font-family:"Roboto Condensed",sans-serif;font-weight:700;font-size:34px;letter-spacing:2px;color:var(--ink)}
.h-sub{font-family:"Roboto Condensed",sans-serif;font-weight:700;font-size:22px;letter-spacing:1px;color:var(--ink)}
.h-glow{font-family:"Roboto Condensed",sans-serif;font-weight:700;font-size:44px;letter-spacing:14px;color:var(--honey)}
.section-dark .h-sub{color:var(--white)}
.body-copy{font-size:13px;line-height:19px;color:var(--muted);width:760px;margin:0 auto}
.section-dark .body-copy{color:#c9c6c2}
.btn-dark{width:144px;height:32px;background:var(--ink);color:var(--white)}

/* welcome */
.welcome{top:718px;height:448px;padding-top:46px}
.welcome .body-copy{margin-top:14px}
.welcome .body-copy+.body-copy{margin-top:18px}
.welcome .btn{margin-top:20px}

/* services */
.services{top:1166px;height:582px;padding-top:24px}
.card-row{position:absolute;left:220px;display:flex;gap:20px}
.service-card{width:242px;height:364px;background:var(--honey)}
.card-photo{width:100%;height:192px}
.service-card h3{font-family:"Roboto Condensed",sans-serif;font-weight:700;font-size:14px;color:var(--ink);margin-top:26px}
.service-card p{font-size:11px;line-height:16px;color:var(--ink);width:196px;margin:14px auto 0}
.service-card .more{display:block;font-family:"Roboto Condensed",sans-serif;font-weight:700;font-size:12px;color:var(--ink);margin-top:20px;text-decoration:none}

/* contact */
.contact{top:1748px;height:480px;padding-top:42px}
.contact .body-copy{margin-top:12px}
.role{font-family:"Roboto Condensed",sans-serif;font-weight:700;font-size:20px;letter-spacing:1px;color:var(--ink);margin-top:18px}
.line{display:flex;justify-content:center;align-items:baseline;gap:26px;color:var(--ink)}
.phone{font-family:"Roboto Condensed",sans-serif;font-weight:700;font-size:30px;letter-spacing:1.5px}
.mail{font-family:"Roboto Condensed",sans-serif;font-weight:700;font-size:15px;letter-spacing:.6px;text-transform:uppercase}
.person{font-family:"Roboto Condensed",sans-serif;font-weight:700;font-size:20px;letter-spacing:1px}
.contact .btn{margin-top:20px}

/* products */
.products{top:2228px;height:460px;padding-top:26px}
.product-row{top:2398px}
.product-card{width:242px}
.product-card .card-photo{height:196px}
.product-label{height:40px;background:var(--honey);display:flex;align-items:center;justify-content:center;font-family:"Roboto Condensed",sans-serif;font-weight:700;font-size:14px;color:var(--ink)}
.slider-dots{position:absolute;left:0;width:1200px;display:flex;justify-content:center;gap:12px}
.slider-dots span{width:6px;height:6px;border-radius:50%;background:var(--honey)}

/* testimonial */
.testimonial{top:2688px;height:248px;background:linear-gradient(90deg,#d49a12,#e9c12a 40%,#f0cf3c 60%,#c9901a)}
.avatar{position:absolute;left:566px;top:18px;width:68px;height:68px;border-radius:50%;background:#e8e2d8;border:3px solid var(--white)}
.quote{position:absolute;left:260px;top:108px;width:680px;font-family:"Roboto Condensed",sans-serif;font-style:italic;font-size:15px;line-height:20px;color:var(--white);letter-spacing:.3px}
.quote-mark{position:absolute;top:98px;font-family:"Roboto Condensed",sans-serif;font-weight:700;font-size:30px;color:var(--ink)}
.author{position:absolute;left:0;top:200px;width:1200px;font-family:"Roboto Condensed",sans-serif;font-weight:700;font-size:14px;letter-spacing:2px;color:var(--white)}

/* footer */
.site-footer{position:absolute;top:2936px;left:0;width:1200px;height:44px;background:var(--ink);display:flex;align-items:center;justify-content:center;font-size:9px;letter-spacing:1px;color:#cfcfcf}
</style>
</head>
<body>

<header class="site-header">
  <div class="brand"><span class="brand-mark"></span><span class="brand-name">Tideflower Honey NZ Limited</span></div>
  <nav class="main-nav">
    <a href="#">HOME</a><a href="#">MANUKA HONEY</a><a href="#">INGREDIENTS</a><a href="#">OFFERS</a><a href="#">ABOUT US</a><a href="#">INVESTOR</a><a href="#">DISCOVER</a>
  </nav>
</header>

<section class="hero">
  <div class="hero-photo" role="img" aria-label="Jars of manuka honey, honeycomb, bee pollen in wooden scoops and yellow gerbera flowers on a rustic wooden table"></div>
  <div class="hero-copy">
    <div class="hero-welcome">Welcome to</div>
    <h1 class="hero-title">TIDEFLOWER HONEY NZ LIMITED</h1>
    <p class="hero-sub">We are a Manuka honey Wholesale and export<br>company based in New Zealand</p>
  </div>
  <a class="btn btn-shop" href="#">SHOP NOW</a>
  <div class="hero-dots"><span></span><span></span><span></span></div>
</section>

<section class="section section-light welcome">
  <h2 class="h-main">WELCOME TIDEFLOWER HONEY NZ LIMITED</h2>
  <h3 class="h-sub">MANUKA HONEY WHOLESALE EXPORT BASED IN NEW ZEALAND</h3>
  <p class="body-copy">Lorem ipsum dolor sitamet, consectetur adipiscingenas suscipit placerat aliquipsumam. Donec ut metusaerat fermentum aliquam et sit amet lectus. Sed tincidunt dui et quam sagittis malesuada. Phasellus a posuere metusm iaculis quam sed augue mollis volutpat. Aenean nec lacus et massa faucibus posuere sed luctus dolor Donec non magna finibus, interdum ex ac, semper dui. Maecenas sollicitudin libero non dui volutpat interdum. Nunc vel ligula consectetur, viverra augue quis, pharetra orci. Suspendisse potenti.</p>
  <p class="body-copy">Pellentesque in egestas turpis. Vivamus at fermentum felis. Phasellus convallis quam in interdum egestas. Aliquam tincidunt venenatis nulla ut ullamcorper.</p>
  <p class="body-copy">Sed blandit neque erat, ut pretium elit egestas non. Mauris auctor et risus non suscipit. Aliquam ut fringilla sapien. In in pulvinar sem, at condimentum odio. Proin tempor nunc massa, eget pharetra magna viverra utEtiam in ornare nisl. Vestibulum ut dictum libero. Donec ut dolor ut mi efficitur pellentesque at nonnibh Praesent sit amet magna a magna faucibus rhoncus.</p>
  <a class="btn btn-dark" href="#">READ MORE</a>
</section>

<section class="section section-dark services">
  <h2 class="h-glow">OUR SERVICES</h2>
  <h3 class="h-sub">MANUKA HONEY WHOLESALE EXPORT BASED IN NEW ZEALAND</h3>
  <p class="body-copy">Lorem ipsum dolor sitamet, consectetur adipiscingenas suscipit placerat aliquipsumam. Donec ut met usaerat fermentum aliquam et sit amet lttis malesuadaosuere iaculis quam sed augue mollis volutpat.</p>
  <div class="card-row" style="top:156px">
    <article class="service-card">
      <div class="card-photo" role="img" aria-label="Pieces of golden honeycomb stacked on a plate" style="background:linear-gradient(160deg,#7a4a18,#d9901c 55%,#5a3414)"></div>
      <h3>MANUKA HONEY WHOLESALE</h3>
      <p>Lorempum doloritame secteturadipiscin-scingenas suscipit placerat aliquipsuma-monec ut metusaerat fermentum aliquam etem sitlipsum amet pat.</p>
      <a class="more" href="#">MORE</a>
    </article>
    <article class="service-card">
      <div class="card-photo" role="img" aria-label="Honey jar with cloth lid beside honeycomb, bee pollen and a yellow flower" style="background:linear-gradient(160deg,#5a3a1c,#e0a42a 55%,#6a4420)"></div>
      <h3>HIVELARK BULK HONEY</h3>
      <p>Lorempum doloritame secteturadipiscin-genas suscipit placerat aliquipsumamonec ut metusaerat fermentum aliquam etem sitlipsum amet pat.</p>
      <a class="more" href="#">MORE</a>
    </article>
    <article class="service-card">
      <div class="card-photo" role="img" aria-label="Glass bowl of honey with honeycomb and a wooden dipper beside flowers" style="background:linear-gradient(160deg,#4a3a4a,#d8901e 55%,#5a3a22)"></div>
      <h3>PRIMARILY MANUKA</h3>
      <p>Lorempum doloritame secteturadipiscin-genas suscipit placerat aliquipsumamone-clipsum ut metusaerat fermentum aliquam etem sitlipsum amet pat.</p>
      <a class="more" href="#">MORE</a>
    </article>
  </div>
</section>

<section class="section section-light contact">
  <h2 class="h-main">CONTACT DETAILS</h2>
  <h3 class="h-sub">CONTACT DETAILS FOR EXPORT AND WHOLESALE INQUIRIES</h3>
  <p class="body-copy">Lorem ipsum dolor sitamet, consectetur adipiscingenas suscipit placerat aliquipsumamonec ut metusaerat fermentum aliquam et sit amet lectus. Sed tincidunt dui et quam sagittis malesuada.</p>
  <p class="role">DESMOND HARLOW EXPORT MANAGER</p>
  <div class="line"><span class="phone">+64 21 438 190</span><span class="mail">dkharlow@pelmail.co.nz</span></div>
  <p class="body-copy" style="margin-top:14px">Sed blandit neque erat, ut pretium elit egestas non sapienInn pulvinar sem, at condimentum odioroin templipsu or nunc massara magna viverra efficitur pellentesque at nonnibht magna a magna faucibus rhoncus.</p>
  <p class="role">FARMERS MARKET WE SUPPLY OUR PRODUCT</p>
  <div class="line" style="margin-top:4px"><span class="person">NEIL FORBES</span><span class="phone">+64 21 067 4183</span></div>
  <div class="mail" style="font-size:13px;color:var(--ink)">tideflowernz@mailpost.com</div>
  <a class="btn btn-dark" href="#">READ MORE</a>
</section>

<section class="section section-dark products">
  <h2 class="h-glow">OUR PRODUCTS</h2>
  <h3 class="h-sub">MANUKA HONEY WHOLESALE EXPORT BASED IN NEW ZEALAND</h3>
  <p class="body-copy">Lorem ipsum dolor sitamet, consectetur adipiscingenas suscipit placerat aliquipsumam. Donec ut met usaerat fermentum aliquam et sit amet lttis malesuadaosuere iaculis quam sed augue mollis volutpat.</p>
  <div class="card-row" style="top:170px;gap:14px">
    <article class="product-card">
      <div class="card-photo" role="img" aria-label="Honeycomb beside a jar of honey and bee pollen" style="background:linear-gradient(160deg,#6a4418,#e0a020 55%,#5a3a16)"></div>
      <div class="product-label">TIDEFLOWER HONEY PRODUCT</div>
    </article>
    <article class="product-card" style="width:244px">
      <div class="card-photo" role="img" aria-label="Bowl of honeycomb with lavender on a dark table" style="background:linear-gradient(160deg,#3a2c3a,#c8861e 55%,#4a3020)"></div>
      <div class="product-label">TIDEFLOWER HONEY PRODUCT</div>
    </article>
    <article class="product-card">
      <div class="card-photo" role="img" aria-label="Honey dripping from a dipper onto a slice of honeycomb" style="background:linear-gradient(160deg,#4a3450,#e8a62a 55%,#6a4420)"></div>
      <div class="product-label">TIDEFLOWER HONEY PRODUCT</div>
    </article>
  </div>
  <div class="slider-dots" style="top:433px"><span></span><span></span><span></span></div>
</section>

<section class="section testimonial" role="img" aria-label="Honeycomb and golden honey in warm yellow light">
  <div class="avatar" role="img" aria-label="Customer portrait"></div>
  <span class="quote-mark" style="left:254px">&ldquo;</span>
  <p class="quote">Allure Pouls estibulum utvehicula metusque vehicula interdunt aliquotesque habitant morbi tristique senectus et netus et malesuadaaugue mollisaenent vulputate commodo nibh eu sodales erat ullamcorper vitae.</p>
  <span class="quote-mark" style="left:924px">&rdquo;</span>
  <p class="author">CALLUM BRECK</p>
</section>

<footer class="site-footer">Copyright &copy; 2017 TIDEFLOWER HONEY NZ LIMITED. All Right Reserved</footer>

</body>
</html>
```